Lantern Motion for Neighbors Business Cards

I need business cards for staff in a new startup. Our company name is Movrela - we train Tai Chi teachers. But our biggest project is called Lantern Motion for Neighbors - a federal project to put together free Tai Chi classes for Vets all across America. It's a young company, with a spirit of excitement, passion, a desire to do good for others (our Vets) and a modern style and sensibility. In other words, not old-fashioned Asian martial arts theme, but something new.

Industry/Entity Type

Health And Wellness

Contact Information for Business Card

The topic is ancient healing, but the company is the Pembrooks - so I'd like a card design that captures that.

Font styles to use
Sans Serif

Colors

Designer to choose colors to be used in the design.

Requirements
Nice to have
• I've got two logos - one for the company and one for the project. I want to see if we can incorporate them both without it becoming too busy.
Should not have
• Overly old-fashioned yin-yang themes.

```html
<!DOCTYPE html>
<html lang="en">
<head>
<meta charset="utf-8">
<title>Lantern Motion for Neighbors – Business Cards</title>
<link rel="stylesheet" href="https://fonts.googleapis.com/css2?family=Montserrat:wght@300;400;500&display=swap">
<style>
  :root {
    --page: #2b2b2b;
    --card-black: #050505;
    --card-white: #ffffff;
    --navy: #3b3a8f;
    --red: #e3202b;
    --white: #ffffff;
  }
  * { margin: 0; padding: 0; box-sizing: border-box; }
  html, body { width: 1200px; height: 900px; overflow: hidden; }
  body {
    background: var(--page);
    font-family: "Montserrat", sans-serif;
    display: flex;
    flex-direction: column;
    align-items: center;
    justify-content: center;
    gap: 40px;
  }
  .card {
    width: 700px;
    height: 400px;
    background: var(--card-black);
    position: relative;
    display: flex;
    box-shadow: 0 10px 24px rgba(0,0,0,0.45);
  }

  /* Front */
  .front-company {
    width: 230px;
    background: var(--card-white);
    display: flex;
    align-items: center;
    justify-content: center;
    gap: 12px;
  }
  .front-company .dot {
    width: 22px; height: 22px; border-radius: 50%;
    background: var(--red);
  }
  .front-company .name {
    color: var(--red);
    font-weight: 500;
    font-size: 30px;
    letter-spacing: 1px;
  }
  .front-project {
    flex: 1;
    display: flex;
    align-items: center;
    justify-content: center;
    gap: 20px;
    padding-bottom: 40px;
  }
  .front-project .ring {
    width: 92px; height: 92px; border-radius: 50%;
    border: 3px solid var(--white);
    flex-shrink: 0;
  }
  .front-project .name {
    color: var(--white);
    font-weight: 300;
    font-size: 28px;
    line-height: 1.15;
    letter-spacing: 1px;
    text-transform: uppercase;
    width: 240px;
  }

  /* Back */
  .back { align-items: center; padding-left: 150px; }
  .back-mark {
    width: 130px;
    display: flex;
    flex-direction: column;
    align-items: center;
    gap: 10px;
  }
  .back-mark .ring {
    width: 110px; height: 110px; border-radius: 50%;
    border: 3px solid var(--navy);
  }
  .back-mark .name {
    color: var(--navy);
    font-size: 11px;
    font-weight: 400;
    text-align: center;
    text-transform: uppercase;
    letter-spacing: 0.5px;
  }
  .divider {
    width: 2px; height: 130px;
    background: var(--navy);
    margin: 0 24px 0 20px;
  }
  .contact { display: flex; flex-direction: column; }
  .person {
    color: var(--navy);
    font-size: 20px;
    font-weight: 400;
    text-transform: uppercase;
    letter-spacing: 0.5px;
  }
  .role {
    color: var(--red);
    font-size: 15px;
    font-weight: 400;
    margin-top: 2px;
  }
  .dash { width: 10px; height: 2px; background: var(--red); margin: 16px 0 10px 4px; }
  .contact-list { list-style: none; display: flex; flex-direction: column; gap: 6px; }
  .contact-list li {
    display: flex; align-items: center; gap: 10px;
    color: var(--navy);
    font-size: 15px;
  }
  .contact-list svg { width: 16px; height: 16px; flex-shrink: 0; }
</style>
</head>
<body>

<section class="card front">
  <div class="front-company">
    <span class="dot"></span>
    <span class="name">Movrela</span>
  </div>
  <div class="front-project">
    <span class="ring"></span>
    <span class="name">Lantern Motion for Neighbors</span>
  </div>
</section>

<section class="card back">
  <div class="back-mark">
    <span class="ring"></span>
    <span class="name">Lantern Motion for Neighbors</span>
  </div>
  <span class="divider"></span>
  <div class="contact">
    <p class="person">Dana Whitlow</p>
    <p class="role">Founder &amp; CEO</p>
    <span class="dash"></span>
    <ul class="contact-list">
      <li>
        <svg viewBox="0 0 16 16" fill="none" stroke="#e3202b" stroke-width="1.4"><path d="M4 2l2.5 3-1.5 1.5c.8 1.8 2.2 3.2 4 4L10.5 9 13.5 11.5 12 14C7 13.5 2.5 9 2 4z"/></svg>
        +01 555 014 7720
      </li>
      <li>
        <svg viewBox="0 0 16 16" fill="none" stroke="#e3202b" stroke-width="1.4"><rect x="2" y="3.5" width="12" height="9"/><path d="M2 3.5l6 5 6-5"/></svg>
        info@movrelastudio.com
      </li>
      <li>
        <svg viewBox="0 0 16 16" fill="none" stroke="#e3202b" stroke-width="1.3"><circle cx="8" cy="8" r="6"/><ellipse cx="8" cy="8" rx="2.6" ry="6"/><path d="M2 8h12"/></svg>
        info.movrelastudio.com
      </li>
    </ul>
  </div>
</section>

</body>
</html>
```